Business Card

Please design a business card with our logo on a cream coloured background and include the following information:

Tallowmere Shopping Centre
ph (08) 9341 7086

sales@velvetpetalblooms.com

www.velvetpetalblooms.com

on reverse:

Find us on Leafnet
facebook.com/velvetpetalblooms

```html
<!DOCTYPE html>
<html lang="en">
<head>
<meta charset="utf-8">
<title>Velvet Petal Blooms – Business Card</title>
<link href="https://fonts.googleapis.com/css2?family=Signika:wght@400;600&display=swap" rel="stylesheet">
<style>
  :root {
    --cream: #ebe5cd;
    --cream-shade: #dcd4b6;
    --green: #3f8a2e;
    --green-dark: #2f6e22;
    --ink: #3b3f4b;
    --on-green: #f1ecd6;
    --page: #efece6;
  }
  * { margin: 0; padding: 0; box-sizing: border-box; }
  html, body {
    width: 1200px; height: 1024px; overflow: hidden;
    background: var(--page);
    font-family: "Signika", sans-serif;
  }
  .card {
    position: absolute; left: 250px;
    width: 700px; height: 400px;
    background: linear-gradient(135deg, var(--cream), var(--cream-shade));
    box-shadow: 0 6px 18px rgba(0,0,0,.18);
    overflow: hidden;
  }
  .card--front { top: 70px; }
  .card--back { top: 554px; }

  /* Front */
  .brand {
    position: absolute; left: 0; right: 0; top: 70px;
    display: flex; flex-direction: column; align-items: center; gap: 18px;
  }
  .brand__dot {
    width: 110px; height: 92px; border-radius: 50%;
    border: 5px solid var(--green);
  }
  .brand__name {
    font-size: 58px; font-weight: 600; color: var(--ink); letter-spacing: .5px;
    white-space: nowrap;
  }
  .social {
    position: absolute; left: 0; right: 0; bottom: 56px;
    display: flex; align-items: center; gap: 18px;
  }
  .social__bar { height: 26px; background: var(--green); }
  .social__bar--lead { width: 120px; }
  .social__bar--tail { flex: 1; }
  .social__text { font-size: 21px; color: var(--ink); white-space: nowrap; }
  .social__network { font-weight: 600; color: var(--green); }

  /* Back */
  .back__head {
    position: absolute; left: 0; right: 0; top: 0; height: 128px;
    display: flex; align-items: center; justify-content: space-between;
    padding: 0 44px;
  }
  .back__name { font-size: 38px; font-weight: 600; color: var(--ink); white-space: nowrap; }
  .back__dot {
    width: 80px; height: 68px; border-radius: 50%;
    border: 4px solid var(--green);
  }
  .back__band {
    position: absolute; left: 0; right: 0; top: 128px; bottom: 0;
    background: linear-gradient(135deg, var(--green), var(--green-dark));
  }
  .back__ghost {
    position: absolute; left: -70px; top: 30px;
    width: 260px; height: 260px; border-radius: 50%;
    border: 14px solid rgba(255,255,255,.08);
  }
  .contact {
    position: absolute; left: 250px; top: 42px;
    list-style: none; color: var(--on-green);
  }
  .contact__place { font-size: 26px; font-weight: 600; margin-bottom: 18px; }
  .contact__line {
    display: flex; align-items: center; gap: 14px;
    font-size: 20px; margin-bottom: 12px;
  }
  .contact__icon { width: 18px; height: 18px; flex: none; }
</style>
</head>
<body>

<section class="card card--front" aria-label="Card front">
  <div class="brand">
    <span class="brand__dot"></span>
    <span class="brand__name">Velvet Petal Blooms</span>
  </div>
  <div class="social">
    <span class="social__bar social__bar--lead"></span>
    <span class="social__text">Find Us On <span class="social__network">Leafnet</span> /velvetpetalblooms</span>
    <span class="social__bar social__bar--tail"></span>
  </div>
</section>

<section class="card card--back" aria-label="Card back">
  <header class="back__head">
    <span class="back__name">Velvet Petal Blooms</span>
    <span class="back__dot"></span>
  </header>
  <div class="back__band">
    <span class="back__ghost"></span>
    <ul class="contact">
      <li class="contact__place">Tallowmere Shopping Centre</li>
      <li class="contact__line">
        <svg class="contact__icon" viewBox="0 0 24 24" fill="currentColor"><path d="M6.6 10.8a15 15 0 0 0 6.6 6.6l2.2-2.2a1 1 0 0 1 1-.25 11.4 11.4 0 0 0 3.6.57 1 1 0 0 1 1 1V20a1 1 0 0 1-1 1A17 17 0 0 1 3 4a1 1 0 0 1 1-1h3.5a1 1 0 0 1 1 1c0 1.25.2 2.45.57 3.57a1 1 0 0 1-.25 1z"/></svg>
        (08) 9341 7086
      </li>
      <li class="contact__line">
        <svg class="contact__icon" viewBox="0 0 24 24" fill="currentColor"><path d="M3 5h18v14H3z M4.5 6.5 12 12l7.5-5.5" stroke="var(--green)" stroke-width="1.5"/></svg>
        sales@velvetpetalblooms.com
      </li>
      <li class="contact__line">
        <svg class="contact__icon" viewBox="0 0 24 24" fill="none" stroke="currentColor" stroke-width="2"><circle cx="12" cy="12" r="9"/><path d="M3 12h18M12 3c3 3 3 15 0 18M12 3c-3 3-3 15 0 18"/></svg>
        www.velvetpetalblooms.com
      </li>
    </ul>
  </div>
</section>

</body>
</html>
```